Re-Design the flow of the Orvane Framework

The orvane framework is a 10 step model that helps teams/organizations become high performing. Attached the model which i created. I love the design as it is but i used a template i don't owe the rights of so i would like to use this platform to see what you can come up with the redesign this flow while keeping the key elements in place. I like the flow, i like the cleanness and i like it to be compact.

Target Market(s)

Organizational change / Leadership/ Consultancy

Industry/Entity Type

Leadership

Requirements
Must have
• Keep as much as possible the flow and feel of the attached
Nice to have
• -Maybe some twist in how the different parts connect (not a must)
Should not have
• Less or more steps than added in the attached file

```html
<!DOCTYPE html>
<html lang="en">
<head>
<meta charset="utf-8">
<title>The Orvane Framework</title>
<link rel="stylesheet" href="https://fonts.googleapis.com/css2?family=Montserrat:wght@500;600;700;800;900&display=swap">
<style>
  :root {
    --dark: #3d3d43;
    --blue: #1f74bf;
    --title: #111318;
    --field: #dde0f0;
    --ink: #363b58;
    --purpose: #8cc63f;
    --vision: #27b3c6;
    --strategy: #1f9ad6;
    --cultivate: #1d6fc0;
    --motivation: #574fb0;
    --growth: #6a3fa0;
    --feedback: #9b3a9e;
    --empower: #e22b6a;
    --perform: #f36f21;
    --monitor: #f7b51b;
    --gold: #c8960c;
    --rule: #e2e3ee;
  }
  * { margin: 0; padding: 0; box-sizing: border-box; }
  html, body { width: 1200px; height: 1200px; overflow: hidden; }
  body { position: relative; background: var(--field); font-family: "Montserrat", sans-serif; }
  .band-top { position: absolute; left: 0; top: 0; width: 1200px; height: 130px; background: var(--dark); }
  .title-strip { position: absolute; left: 0; top: 130px; width: 1200px; height: 86px; background: #fff; display: flex; align-items: center; justify-content: center; }
  .title { font-weight: 800; font-size: 56px; letter-spacing: -0.5px; color: var(--title); line-height: 1; }
  .title .accent { color: var(--blue); }
  .subtitle-strip { position: absolute; left: 0; top: 216px; width: 1200px; height: 36px; background: var(--blue); display: flex; align-items: center; padding-left: 70px; }
  .subtitle { color: #fff; font-weight: 700; font-size: 17.5px; letter-spacing: 0.2px; text-transform: uppercase; }
  .rule-bottom { position: absolute; left: 0; top: 1048px; width: 1200px; height: 10px; background: var(--blue); }
  .band-bottom { position: absolute; left: 0; top: 1058px; width: 1200px; height: 142px; background: var(--dark); }
  .diagram { position: absolute; left: 0; top: 0; width: 1200px; height: 1200px; }
  .diagram text { font-family: "Montserrat", sans-serif; }
  .seg-label { font-weight: 700; font-size: 15px; fill: #fff; letter-spacing: 0.6px; }
  .ring-label { font-weight: 800; font-size: 16px; fill: #fff; letter-spacing: 0.8px; }
  .step-text { font-weight: 500; font-size: 11.5px; fill: var(--ink); text-anchor: middle; }
  .goal-head { font-weight: 800; font-size: 17px; fill: var(--gold); text-anchor: middle; }
  .goal-list { font-weight: 700; font-size: 11px; fill: #2b3150; }
  .restart { font-weight: 800; font-size: 13px; fill: var(--purpose); }
  .restart-soft { font-weight: 800; font-size: 13px; fill: #8fa2c8; }
  .loop-label { font-weight: 800; font-size: 15px; }
  .icon-glyph { fill: none; stroke: #fff; stroke-width: 2.2; stroke-linecap: round; stroke-linejoin: round; }
</style>
</head>
<body>
  <div class="band-top"></div>
  <header class="title-strip">
    <h1 class="title">THE <span class="accent">ORVANE</span> FRAMEWORK</h1>
  </header>
  <div class="subtitle-strip">
    <p class="subtitle">Liberate the workplace unleashing value through purpose at every level of scale</p>
  </div>
  <div class="rule-bottom"></div>
  <div class="band-bottom"></div>

  <svg class="diagram" viewBox="0 0 1000 1000" xmlns="http://www.w3.org/2000/svg" aria-label="Ten step flow of the Orvane Framework">
    <defs>
      <linearGradient id="ring-left" gradientUnits="userSpaceOnUse" x1="80" y1="800" x2="600" y2="250">
        <stop offset="0" stop-color="#d3d6e8"/>
        <stop offset="0.35" stop-color="#3f86cf"/>
        <stop offset="0.7" stop-color="#6a62bb"/>
        <stop offset="1" stop-color="#cfcde6"/>
      </linearGradient>
      <linearGradient id="ring-right" gradientUnits="userSpaceOnUse" x1="430" y1="720" x2="960" y2="600">
        <stop offset="0" stop-color="#c4c6da"/>
        <stop offset="0.5" stop-color="#a5a8c2"/>
        <stop offset="1" stop-color="#dcdcea"/>
      </linearGradient>
      <linearGradient id="gold-loop" gradientUnits="userSpaceOnUse" x1="580" y1="440" x2="780" y2="540">
        <stop offset="0" stop-color="#b38209"/>
        <stop offset="1" stop-color="#f4b923"/>
      </linearGradient>
      <linearGradient id="start-arrow" x1="0" y1="0" x2="0" y2="1">
        <stop offset="0" stop-color="#9bd04a"/>
        <stop offset="1" stop-color="#7fb935"/>
      </linearGradient>
      <path id="left-cw" d="M551,530 A221,221 0 1 1 109,530 A221,221 0 1 1 551,530"/>
      <path id="left-ccw" d="M330,296 A234,234 0 1 0 330,764 A234,234 0 1 0 330,296"/>
      <path id="left-ring-cw" d="M600,530 A270,270 0 1 1 60,530 A270,270 0 1 1 600,530"/>
      <path id="right-ccw" d="M672,291 A244,244 0 1 0 672,779 A244,244 0 1 0 672,291"/>
      <path id="right-ring-ccw" d="M672,249 A286,286 0 1 0 672,821 A286,286 0 1 0 672,249"/>
    </defs>

    <!-- outer guide rings -->
    <circle cx="672" cy="535" r="280" fill="none" stroke="url(#ring-right)" stroke-width="24" pathLength="360" stroke-dasharray="125 235" transform="rotate(15 672 535)"/>
    <circle cx="330" cy="530" r="275" fill="none" stroke="url(#ring-left)" stroke-width="26" pathLength="360" stroke-dasharray="200 160" transform="rotate(120 330 530)"/>

    <!-- engagement wheel base -->
    <g class="wheel-right">
      <circle cx="672" cy="535" r="218" fill="#fff"/>
      <circle cx="672" cy="535" r="238" fill="none" stroke="var(--empower)" stroke-width="40" pathLength="360" stroke-dasharray="39 321" transform="rotate(95.6 672 535)"/>
      <circle cx="672" cy="535" r="238" fill="none" stroke="var(--perform)" stroke-width="40" pathLength="360" stroke-dasharray="44 316" transform="rotate(50.6 672 535)"/>
      <circle cx="672" cy="535" r="238" fill="none" stroke="var(--monitor)" stroke-width="40" pathLength="360" stroke-dasharray="64 296" transform="rotate(345.6 672 535)"/>
      <g stroke="var(--rule)" stroke-width="1.5">
        <line x1="762" y1="535" x2="890" y2="535" transform="rotate(50 672 535)"/>
        <line x1="762" y1="535" x2="890" y2="535" transform="rotate(95 672 535)"/>
        <line x1="762" y1="535" x2="890" y2="535" transform="rotate(135 672 535)"/>
      </g>
      <circle cx="672" cy="535" r="79" fill="none" stroke="var(--feedback)" stroke-width="16" pathLength="360" stroke-dasharray="44 316" transform="rotate(135.6 672 535)"/>
      <circle cx="672" cy="535" r="79" fill="none" stroke="var(--empower)" stroke-width="16" pathLength="360" stroke-dasharray="39 321" transform="rotate(95.6 672 535)"/>
      <circle cx="672" cy="535" r="79" fill="none" stroke="var(--perform)" stroke-width="16" pathLength="360" stroke-dasharray="44 316" transform="rotate(50.6 672 535)"/>
      <circle cx="672" cy="535" r="79" fill="none" stroke="var(--monitor)" stroke-width="16" pathLength="360" stroke-dasharray="64 296" transform="rotate(345.6 672 535)"/>
      <circle cx="672" cy="535" r="70" fill="#fff" stroke="#e6e7f1" stroke-width="2"/>
    </g>

    <!-- self direction wheel -->
    <g class="wheel-left">
      <circle cx="330" cy="530" r="102.5" fill="none" stroke="#fff" stroke-width="205" pathLength="360" stroke-dasharray="270 90" transform="rotate(95 330 530)"/>
      <circle cx="330" cy="530" r="227.5" fill="none" stroke="var(--purpose)" stroke-width="45" pathLength="360" stroke-dasharray="52 308" transform="rotate(95.6 330 530)"/>
      <circle cx="330" cy="530" r="227.5" fill="none" stroke="var(--vision)" stroke-width="45" pathLength="360" stroke-dasharray="39 321" transform="rotate(148.6 330 530)"/>
      <circle cx="330" cy="530" r="227.5" fill="none" stroke="var(--strategy)" stroke-width="45" pathLength="360" stroke-dasharray="39 321" transform="rotate(188.6 330 530)"/>
      <circle cx="330" cy="530" r="227.5" fill="none" stroke="var(--cultivate)" stroke-width="45" pathLength="360" stroke-dasharray="43 317" transform="rotate(228.6 330 530)"/>
      <circle cx="330" cy="530" r="227.5" fill="none" stroke="var(--motivation)" stroke-width="45" pathLength="360" stroke-dasharray="45 315" transform="rotate(272.6 330 530)"/>
      <circle cx="330" cy="530" r="227.5" fill="none" stroke="var(--growth)" stroke-width="45" pathLength="360" stroke-dasharray="46 314" transform="rotate(318.6 330 530)"/>
      <g stroke="var(--rule)" stroke-width="1.5">
        <line x1="420" y1="530" x2="535" y2="530" transform="rotate(148 330 530)"/>
        <line x1="420" y1="530" x2="535" y2="530" transform="rotate(188 330 530)"/>
        <line x1="420" y1="530" x2="535" y2="530" transform="rotate(228 330 530)"/>
        <line x1="420" y1="530" x2="535" y2="530" transform="rotate(272 330 530)"/>
        <line x1="420" y1="530" x2="535" y2="530" transform="rotate(318 330 530)"/>
      </g>
      <circle cx="330" cy="530" r="79" fill="none" stroke="var(--purpose)" stroke-width="16" pathLength="360" stroke-dasharray="52 308" transform="rotate(95.6 330 530)"/>
      <circle cx="330" cy="530" r="79" fill="none" stroke="var(--vision)" stroke-width="16" pathLength="360" stroke-dasharray="39 321" transform="rotate(148.6 330 530)"/>
      <circle cx="330" cy="530" r="79" fill="none" stroke="var(--strategy)" stroke-width="16" pathLength="360" stroke-dasharray="39 321" transform="rotate(188.6 330 530)"/>
      <circle cx="330" cy="530" r="79" fill="none" stroke="var(--cultivate)" stroke-width="16" pathLength="360" stroke-dasharray="43 317" transform="rotate(228.6 330 530)"/>
      <circle cx="330" cy="530" r="79" fill="none" stroke="var(--motivation)" stroke-width="16" pathLength="360" stroke-dasharray="45 315" transform="rotate(272.6 330 530)"/>
      <circle cx="330" cy="530" r="79" fill="none" stroke="var(--growth)" stroke-width="16" pathLength="360" stroke-dasharray="46 314" transform="rotate(318.6 330 530)"/>
      <circle cx="330" cy="530" r="70" fill="#fff" stroke="#e6e7f1" stroke-width="2"/>
    </g>

    <!-- feedback segment crossing over -->
    <g class="seg-feedback">
      <circle cx="672" cy="535" r="238" fill="none" stroke="var(--feedback)" stroke-width="40" pathLength="360" stroke-dasharray="44 316" transform="rotate(135.6 672 535)"/>
    </g>

    <!-- back to purpose loop -->
    <g class="loop-back">
      <circle cx="672" cy="535" r="104" fill="none" stroke="url(#gold-loop)" stroke-width="32" pathLength="360" stroke-dasharray="110 250" transform="rotate(236 672 535)"/>
      <polygon points="626.1,469.5 598.5,430.2 586.1,468.2" fill="#b38209"/>
      <text class="loop-label" transform="translate(605 405) rotate(-62)"><tspan fill="#a7b0cf">BACK TO</tspan><tspan x="0" dy="17" fill="var(--purpose)">PURPOSE</tspan></text>
    </g>

    <!-- full potential badge -->
    <g class="goal">
      <polyline points="740,410 740,320 802,320" fill="none" stroke="var(--gold)" stroke-width="1.6" stroke-dasharray="2 3"/>
      <circle cx="740" cy="452" r="40" fill="#c8960c" stroke="#fff" stroke-width="4"/>
      <g class="icon-glyph" stroke-width="2.4" transform="translate(-30 2)">
        <polygon points="748,440 756,428 784,428 792,440 770,470"/>
        <polyline points="748,440 792,440"/>
        <polyline points="762,428 758,440 770,470 782,440 778,428"/>
      </g>
      <text class="goal-head"><tspan x="880" y="246">REACHING</tspan><tspan x="880" y="268">FULL POTENTIAL</tspan><tspan x="880" y="290">OF PEOPLE</tspan><tspan x="880" y="312">&amp; ORGANIZATION</tspan></text>
      <text class="goal-list"><tspan x="806" y="328">• Productivity up to 800%</tspan><tspan x="806" y="343">• Employee Management &gt; 90%</tspan><tspan x="806" y="358">• Max discretionary effort gap</tspan><tspan x="806" y="373">• High resilience to change</tspan></text>
    </g>

    <!-- start arrow -->
    <g class="start">
      <path d="M342,776 L470,760 L466,790 L456,798 L434,846 L340,798 Z" fill="url(#start-arrow)"/>
      <rect x="350" y="666" width="52" height="15" rx="2" fill="var(--purpose)"/>
      <text x="376" y="677" text-anchor="middle" font-size="9" font-weight="800" fill="#fff">START</text>
      <polygon points="362,708 370,686 382,686 390,708" fill="var(--purpose)"/>
      <line x1="376" y1="689" x2="376" y2="706" stroke="#fff" stroke-width="1.6" stroke-dasharray="3 3"/>
      <text class="restart" x="350" y="726">RE-START</text>
      <text class="restart" x="350" y="741">RE-INVENT</text>
      <text class="restart-soft" x="350" y="756">HERE</text>
    </g>

    <!-- ring labels -->
    <text class="ring-label"><textPath href="#left-ring-cw" startOffset="51%" text-anchor="middle">SELF DIRECTION ▸▸</textPath></text>
    <text class="ring-label"><textPath href="#left-ring-cw" startOffset="81%" text-anchor="middle">HUMAN EXPERIENCE ▸▸▸</textPath></text>
    <text class="ring-label"><textPath href="#right-ring-ccw" startOffset="50%" text-anchor="middle">UNLEASH ENGAGEMENTS ▸▸▸</textPath></text>

    <!-- segment labels -->
    <g class="seg-labels">
      <text class="seg-label"><textPath href="#left-ccw" startOffset="41.25%" text-anchor="middle">PURPOSE</textPath></text>
      <text class="seg-label"><textPath href="#left-cw" startOffset="46.7%" text-anchor="middle">VISION</textPath></text>
      <text class="seg-label"><textPath href="#left-cw" startOffset="57.8%" text-anchor="middle">STRATEGY</textPath></text>
      <text class="seg-label"><textPath href="#left-cw" startOffset="69.4%" text-anchor="middle">CULTIVATE</textPath></text>
      <text class="seg-label"><textPath href="#left-cw" startOffset="81.9%" text-anchor="middle">MOTIVATION</textPath></text>
      <text class="seg-label"><textPath href="#left-cw" startOffset="94.9%" text-anchor="middle">GROWTH</textPath></text>
      <text class="seg-label"><textPath href="#right-ccw" startOffset="31.25%" text-anchor="middle">FEEDBACK</textPath></text>
      <text class="seg-label"><textPath href="#right-ccw" startOffset="43.1%" text-anchor="middle">EMPOWERMENT</textPath></text>
      <text class="seg-label"><textPath href="#right-ccw" startOffset="54.9%" text-anchor="middle">PERFORMANCE</textPath></text>
      <text class="seg-label"><textPath href="#right-ccw" startOffset="70.1%" text-anchor="middle">MONITOR</textPath></text>
    </g>

    <!-- step descriptions -->
    <g class="step-texts">
      <text class="step-text"><tspan x="262" y="672">Discover</tspan><tspan x="262" y="686">your purpose.</tspan><tspan x="262" y="700">Why do you</tspan><tspan x="262" y="714">exist?</tspan></text>
      <text class="step-text"><tspan x="182" y="590">Identify</tspan><tspan x="182" y="604">purpose</tspan><tspan x="182" y="618">activators.</tspan></text>
      <text class="step-text"><tspan x="170" y="467">Develop</tspan><tspan x="170" y="481">a master</tspan><tspan x="170" y="495">plan</tspan></text>
      <text class="step-text"><tspan x="282" y="346">Cultivate</tspan><tspan x="282" y="360">psychological</tspan><tspan x="282" y="374">safety and</tspan><tspan x="282" y="388">ownership.</tspan></text>
      <text class="step-text"><tspan x="394" y="354">Tap into</tspan><tspan x="394" y="368">people's purpose</tspan><tspan x="394" y="382">&amp; passion. (Intrinsic</tspan><tspan x="394" y="396">motivation)</tspan></text>
      <text class="step-text"><tspan x="496" y="470">Unlock</tspan><tspan x="496" y="484">culture of</tspan><tspan x="496" y="498">personal</tspan><tspan x="496" y="512">growth &amp;</tspan><tspan x="496" y="526">development.</tspan></text>
      <text class="step-text"><tspan x="530" y="615">Prioritize</tspan><tspan x="530" y="629">feedback &amp;</tspan><tspan x="530" y="643">transparency.</tspan></text>
      <text class="step-text"><tspan x="594" y="676">Empower the</tspan><tspan x="594" y="690">community from</tspan><tspan x="594" y="704">bottom up.</tspan></text>
      <text class="step-text"><tspan x="720" y="684">Put excellent</tspan><tspan x="720" y="698">(Team) performance</tspan><tspan x="720" y="712">in the spotlight.</tspan></text>
      <text class="step-text"><tspan x="828" y="600">Monitor</tspan><tspan x="828" y="614">engagement</tspan><tspan x="828" y="628">real time.</tspan></text>
    </g>

    <!-- step icons -->
    <g class="step-icons">
      <g transform="translate(292 620)">
        <circle r="22" fill="var(--purpose)" stroke="#fff" stroke-width="3"/>
        <g class="icon-glyph"><circle r="10"/><circle r="4.5"/><path d="M3,-3 L11,-11 M8,-11 H11 V-8"/></g>
      </g>
      <g transform="translate(240 578)">
        <circle r="22" fill="var(--vision)" stroke="#fff" stroke-width="3"/>
        <g class="icon-glyph"><path d="M-12,0 Q0,-10 12,0 Q0,10 -12,0 Z"/><circle r="3.8"/></g>
      </g>
      <g transform="translate(238 492)">
        <circle r="22" fill="var(--strategy)" stroke="#fff" stroke-width="3"/>
        <g class="icon-glyph"><circle r="8.5"/><path d="M0,-13 V-5 M0,5 V13 M-13,0 H-5 M5,0 H13"/></g>
      </g>
      <g transform="translate(288 417)">
        <circle r="22" fill="var(--cultivate)" stroke="#fff" stroke-width="3"/>
        <g class="icon-glyph"><path d="M0,-12 L10,-8 V0 Q10,8 0,12 Q-10,8 -10,0 V-8 Z"/><path d="M-4,0 L-1,3 L5,-4"/></g>
      </g>
      <g transform="translate(370 432)">
        <circle r="22" fill="var(--motivation)" stroke="#fff" stroke-width="3"/>
        <g class="icon-glyph"><path d="M0,10 L-10,0 Q-14,-5 -10,-9 Q-5,-13 0,-7 Q5,-13 10,-9 Q14,-5 10,0 Z"/><path d="M-8,-1 H-4 L-2,-5 L1,3 L3,-1 H8"/></g>
      </g>
      <g transform="translate(430 490)">
        <circle r="22" fill="var(--growth)" stroke="#fff" stroke-width="3"/>
        <g class="icon-glyph"><path d="M0,12 V-2"/><path d="M0,-2 Q-1,-11 -10,-10 Q-10,-2 0,-2 Z"/><path d="M0,2 Q1,-7 10,-6 Q10,2 0,2 Z"/></g>
      </g>
      <g transform="translate(557 576)">
        <circle r="22" fill="var(--feedback)" stroke="#fff" stroke-width="3"/>
        <g class="icon-glyph"><path d="M-11,-9 H11 V5 H-2 L-7,10 V5 H-11 Z"/><path d="M-6,-3 H6 M-6,1 H3"/></g>
      </g>
      <g transform="translate(612 638)">
        <circle r="22" fill="var(--empower)" stroke="#fff" stroke-width="3"/>
        <g class="icon-glyph"><path d="M-8,10 V2 M0,10 V-4 M8,10 V-10"/><path d="M-11,-4 L-2,-11 M-6,-11 H-2 V-7"/></g>
      </g>
      <g transform="translate(680 638)">
        <circle r="22" fill="var(--perform)" stroke="#fff" stroke-width="3"/>
        <g class="icon-glyph"><polygon points="0,-11 3.2,-3.5 11,-3.5 4.8,1.5 7,9.5 0,5 -7,9.5 -4.8,1.5 -11,-3.5 -3.2,-3.5"/></g>
      </g>
      <g transform="translate(765 580)">
        <circle r="22" fill="var(--monitor)" stroke="#fff" stroke-width="3"/>
        <g class="icon-glyph"><circle cx="-2" cy="-2" r="7.5"/><path d="M3.5,3.5 L10,10"/></g>
      </g>
    </g>
  </svg>
</body>
</html>
```